Staff Newsletter Template Image

We are looking for two .jpg images that we can put into a Word document and use for our staff newsletter. We will then add content using text boxes.
Attached is the current template which works for the columns and size that we need but we just want a fresh new design.
The Word document shows how we use it.
The name will stay the same - Team upBeat but can be a different look to the current one.

Target Market(s)

Sales team

Colors

Designer to choose colors to be used in the design.

Requirements
Must have
• Colours will be green, grey and white, possibly cream if needed. All from the guidelines.
• I have attached our brand guidelines which shows design elements and fonts for our brand. Also attached is brand guidelines for one of our product lines as we would like to use the same green.
• It needs to be nice to look at and motivational for our team

```html
<!DOCTYPE html>
<html lang="en">
<head>
<meta charset="utf-8">
<title>Team upBeat – Newsletter Pages</title>
<link rel="stylesheet" href="https://fonts.googleapis.com/css2?family=Lato:wght@300&display=swap">
<style>
  :root {
    --backdrop: #d8d8d8;
    --paper: #ffffff;
    --charcoal: #4c4a4b;
    --leaf: #8cc544;
    --leaf-deep: #578a2a;
  }
  * { margin: 0; padding: 0; box-sizing: border-box; }
  html, body {
    width: 1200px;
    height: 1000px;
    overflow: hidden;
    background: var(--backdrop);
  }
  .canvas {
    position: relative;
    width: 1200px;
    height: 1000px;
  }
  .page {
    position: absolute;
    top: 182px;
    width: 448px;
    height: 633px;
    display: block;
    background: var(--paper);
  }
  .page--front { left: 120px; }
  .page--back { left: 632px; }
  .brand-name {
    font-family: 'Lato', sans-serif;
    font-weight: 300;
    fill: var(--paper);
  }
</style>
</head>
<body>
  <main class="canvas">
    <svg class="page page--front" viewBox="0 0 672 950" role="img" aria-label="Newsletter front page with Team upBeat masthead">
      <defs>
        <linearGradient id="front-wave" x1="0" y1="0" x2="1" y2="0">
          <stop offset="0" stop-color="var(--leaf-deep)"/>
          <stop offset="0.25" stop-color="var(--leaf)"/>
          <stop offset="1" stop-color="var(--leaf)"/>
        </linearGradient>
      </defs>
      <rect class="page-paper" width="672" height="950" fill="var(--paper)"/>
      <rect class="column-accent" x="335" y="100" width="337" height="850" fill="var(--leaf)"/>
      <path class="masthead-wave" d="M0,82 L0,120 C110,140 240,140 335,122 L335,200 L672,200 L672,28 Z" fill="url(#front-wave)"/>
      <path class="masthead-band" d="M0,0 H672 V28 C590,44 540,62 490,80 C400,112 320,128 250,128 C150,128 60,108 0,82 Z" fill="var(--charcoal)"/>
      <text class="brand-name" x="100" y="94" font-size="44">Team upBeat</text>
    </svg>

    <svg class="page page--back" viewBox="0 0 672 950" role="img" aria-label="Newsletter back page">
      <defs>
        <linearGradient id="back-wave" x1="0" y1="0" x2="1" y2="0">
          <stop offset="0" stop-color="var(--leaf-deep)"/>
          <stop offset="1" stop-color="var(--leaf)"/>
        </linearGradient>
      </defs>
      <rect class="page-paper" width="672" height="950" fill="var(--paper)"/>
      <rect class="column-accent" x="337" y="0" width="335" height="950" fill="var(--charcoal)"/>
      <path class="footer-wave" d="M0,928 C70,918 130,896 180,876 C260,846 340,830 430,830 C530,830 610,850 672,876 L672,950 L0,950 Z" fill="url(#back-wave)"/>
    </svg>
  </main>
</body>
</html>
```